business card and letter head for Australian company manufacturing rienforcing steel for constructio

business card and letter head using our logo. you will need to change the name of the logo to KOLVATIN and the red part of the logo needs to start at the e after d.

Architects, Engineers, Builders, Developers

Manufacturing

```html
<!DOCTYPE html>
<html lang="en">
<head>
<meta charset="utf-8">
<title>Kolvatin Letterhead</title>
<link rel="stylesheet" href="https://fonts.googleapis.com/css2?family=Arimo:wght@700&display=swap">
<style>
  :root {
    --ink: #404040;
    --brand-red: #7d2a20;
    --paper: #ffffff;
    --frame: #8a8a8a;
  }
  html, body {
    margin: 0;
    padding: 0;
    width: 927px;
    height: 1200px;
    overflow: hidden;
    background: var(--paper);
  }
  .letterhead {
    position: relative;
    width: 927px;
    height: 1200px;
    box-sizing: border-box;
    border: 1px solid var(--frame);
    background: var(--paper);
    font-family: "Arimo", Arial, sans-serif;
    font-weight: 700;
    color: var(--ink);
  }
  .brand {
    position: absolute;
    left: 44px;
    top: 27px;
  }
  .brand-square {
    position: absolute;
    left: 78px;
    top: 0;
    width: 88px;
    height: 88px;
    background: var(--brand-red);
  }
  .brand-name {
    position: absolute;
    left: 0;
    top: 88px;
    margin: 0;
    font-size: 48px;
    line-height: 1;
    color: var(--ink);
    white-space: nowrap;
  }
  .contact {
    position: absolute;
    right: 49px;
    top: 36px;
    text-align: right;
    line-height: 1;
  }
  .contact-line {
    margin: 0;
    white-space: nowrap;
  }
  .contact-line--major {
    font-size: 24px;
    margin-bottom: 3px;
  }
  .contact-line--minor {
    font-size: 17.5px;
    margin-top: 4px;
  }
  .header-rule {
    position: absolute;
    left: 21px;
    right: 30px;
    top: 171px;
    height: 2.5px;
    background: var(--brand-red);
  }
</style>
</head>
<body>
  <main class="letterhead">
    <header>
      <div class="brand">
        <span class="brand-square" aria-hidden="true"></span>
        <p class="brand-name">kolvatin</p>
      </div>
      <address class="contact" style="font-style: normal;">
        <p class="contact-line contact-line--major">Phone - 07 5550 1284</p>
        <p class="contact-line contact-line--major">Fax - 07 5550 1297</p>
        <p class="contact-line contact-line--minor">email office@kolvatin.com</p>
        <p class="contact-line contact-line--minor">www.kolvatin.com</p>
        <p class="contact-line contact-line--minor">14 Harlow Street Bowen, QLD 4805 Australia</p>
      </address>
      <div class="header-rule" aria-hidden="true"></div>
    </header>
  </main>
</body>
</html>
```